Building company with a modern and unique product looking for a business card to help us stand out

We currently have a logo but as our business has grown, we feel that our business card is not reflecting our modern and high quality product and help us stand out from the crowd. Our business is mainly in the construction of new homes using a unique method and materials that makes our homes fire proof, vermin and pest resistant and rated to the maximum cyclone category (category 5). We need a business card that helps us stand out as well as communicating professionalism, high quality and trustworthiness. I have attached our current logo with a black and white option, as well as our business card which is double sided. We would like to retain as much of the information that is currently on our business cards, but presented in a more sleek way. We do like our current colour palette ( white, black, yellow and grey) and have been looking primarily at business cards with a black background however we are open to other combinations of colour and layout as long as we stand out. Please feel free to tweak our logo to make it more suitable for a business card, we like the black option that we use but we have had trouble trying to get the white area to match the rest of the logo and blend effectively into a business card. Please do not hesitate to contact us with any questions as we really want this to be successful!

Target Market(s)

Large contracts including government and larger companies

Industry/Entity Type

Business

We will be providing this business card to potential clients including key government ministers and large funding companies, our business card should show that we are professional and reliable.

Requirements
Must have
• It must be easy to read and pleasing to the eye, It must contain as much of the information on the current business card and unless something really stands out, we will most likely pick a design that has all of the information included. It must include our logo of course and have some colour included.
Nice to have
• We are looking for a high end business card and would like to see designs that reflect this. We like the gloss/matte contrast, plastic cards with opaque/coloured areas and unique features not seen on everyday paper business cards. It would be nice to see a few different colour combinations, we are open to new ideas so please feel free to take some artistic licence.
Should not have
• Must not be too busy, difficult to read or be distracting from the information conveyed. Other than this please feel free to add your own touches and make it unique!

```html
<!DOCTYPE html>
<html lang="en">
<head>
<meta charset="utf-8">
<title>Corvell Building Company – Business Card</title>
<link href="https://fonts.googleapis.com/css2?family=Libre+Baskerville:ital,wght@0,400;0,700;1,400&family=Open+Sans:ital,wght@0,400;1,400&display=swap" rel="stylesheet">
<style>
  :root {
    --backdrop: #3a3a3a;
    --paper: #f1f1f0;
    --ink: #111111;
    --gold: #c39f2a;
    --gold-text: #c29a2c;
    --grey: #444444;
    --white: #ffffff;
  }
  * { margin: 0; padding: 0; box-sizing: border-box; }
  html, body { width: 1200px; height: 750px; overflow: hidden; }
  body {
    background: var(--backdrop);
    position: relative;
    font-family: "Open Sans", Arial, sans-serif;
  }
  .card {
    position: absolute;
    top: 228px;
    width: 461px;
    height: 263px;
    overflow: hidden;
  }
  .card--front { left: 124px; background: var(--paper); }
  .card--back { left: 618px; background: var(--gold); }

  .wordmark {
    position: absolute;
    left: 0; right: 0;
    text-align: center;
    font-family: "Libre Baskerville", Georgia, serif;
    font-weight: 400;
    color: var(--ink);
    line-height: 1.1;
  }
  .card--front .wordmark { top: 86px; font-size: 25px; }
  .card--back .wordmark { top: 38px; font-size: 25px; }
  .wordmark__square {
    display: inline-block;
    width: 12px; height: 12px;
    background: var(--ink);
    margin-right: 8px;
    vertical-align: 2px;
  }

  .edge-bar { position: absolute; top: 186px; height: 52px; }
  .edge-bar--left { left: 0; width: 7px; background: var(--ink); }
  .edge-bar--right { right: 0; width: 9px; background: var(--gold); }

  .person { position: absolute; left: 28px; top: 188px; }
  .person__name {
    font-family: "Libre Baskerville", Georgia, serif;
    font-weight: 700;
    font-size: 17px;
    letter-spacing: 0.6px;
    color: var(--ink);
  }
  .person__role {
    font-family: "Libre Baskerville", Georgia, serif;
    font-size: 12.5px;
    color: var(--gold-text);
    margin-top: 2px;
  }
  .person__email {
    font-style: italic;
    font-size: 11px;
    color: var(--grey);
    margin-top: 4px;
  }

  .contacts {
    position: absolute;
    right: 34px;
    top: 190px;
    list-style: none;
    text-align: right;
  }
  .contacts li {
    font-size: 11px;
    color: var(--grey);
    height: 17.5px;
    display: flex;
    align-items: center;
    justify-content: flex-end;
    gap: 6px;
  }
  .contacts svg { width: 11px; height: 11px; fill: var(--ink); }

  .roofline-art {
    position: absolute;
    left: 0; right: 0;
    top: 122px;
    height: 115px;
    background: linear-gradient(180deg, var(--gold) 0%, #dcc985 55%, #ece6d2 100%);
  }
  .web-band {
    position: absolute;
    left: 0; right: 0; bottom: 0;
    height: 26px;
    background: var(--ink);
    color: var(--white);
    font-size: 11.5px;
    letter-spacing: 6px;
    text-align: center;
    line-height: 26px;
  }
</style>
</head>
<body>
  <section class="card card--front" aria-label="Card front">
    <div class="wordmark"><span class="wordmark__square"></span>Corvell Building Company</div>

    <span class="edge-bar edge-bar--left"></span>
    <span class="edge-bar edge-bar--right"></span>

    <div class="person">
      <p class="person__name">Dalton Reeves</p>
      <p class="person__role">Managing Director</p>
      <p class="person__email">hello@corvellbuild.com</p>
    </div>

    <ul class="contacts">
      <li>0400 000 123
        <svg viewBox="0 0 24 24" aria-hidden="true"><path d="M6.6 10.8a15 15 0 0 0 6.6 6.6l2.2-2.2a1 1 0 0 1 1-.25 11.4 11.4 0 0 0 3.6.57 1 1 0 0 1 1 1V20a1 1 0 0 1-1 1A17 17 0 0 1 3 4a1 1 0 0 1 1-1h3.5a1 1 0 0 1 1 1c0 1.25.2 2.45.57 3.57a1 1 0 0 1-.25 1z"/></svg>
      </li>
      <li>(02) 5550 0142
        <svg viewBox="0 0 24 24" aria-hidden="true"><path d="M7 1h10a2 2 0 0 1 2 2v18a2 2 0 0 1-2 2H7a2 2 0 0 1-2-2V3a2 2 0 0 1 2-2zm0 3v15h10V4z"/></svg>
      </li>
      <li>www.corvellbuild.com
        <svg viewBox="0 0 24 24" aria-hidden="true"><circle cx="12" cy="12" r="11"/><path d="M12 1v22M1 12h22M4 6h16M4 18h16" stroke="#f1f1f0" stroke-width="1.4" fill="none"/></svg>
      </li>
    </ul>
  </section>

  <section class="card card--back" aria-label="Card back">
    <div class="wordmark"><span class="wordmark__square"></span>Corvell Building Company</div>
    <div class="roofline-art" role="img" aria-label="Large white silhouette of overlapping house rooftops with chimneys and small windows"></div>
    <div class="web-band">www.corvellbuild.com</div>
  </section>
</body>
</html>
```